brindle goods anti snore device

The item is a silicone anti snore device that goes into your nostrils. I need an attractive descriptive design. If a photo from pixelharbor or a free and clear without copyright issue can be used to photo shop in the product that would be awesome. The product is pretty much identical to the following item which I've attached a link http://www.shopvendrix.example/Snoring-BreezaLoop-Sleep-Apnea-Device/dp/K47QX2MZ91/ref=sr_1_1?ie=UTF8&qid=1409110329&sr=8-1&keywords=breezaloop. There are several pictures of the different angles as well as the instructions. I like this packaging but I obviously need to change it around. i think it could be a good reference though.

There is a document for the back instructions. Please show me the back design as well.

Target Market(s)

adults mostly men. should have "sleepy colors"

Industry/Entity Type

Shop

Font styles to use
Serif

Colors
33b7a4
cadf83
85cae6
faee3e
e34197

Requirements
Must have
• sharp with an image
Should not have
• name of "breezaloop" anywhere on it

```html
<!DOCTYPE html>
<html lang="en">
<head>
<meta charset="utf-8">
<title>BrindleGoods Anti Snore Aid – Back Panel</title>
<link href="https://fonts.googleapis.com/css2?family=Tinos:wght@400;700&display=swap" rel="stylesheet">
<style>
  :root {
    --teal: #33b7a4;
    --teal-light: #5fe0d2;
    --lime: #cadf83;
    --sky: #85cae6;
    --rule: #8aa8c0;
    --ink: #111111;
    --brand-ink: #2e2416;
    --heading-blue: #2f8fb5;
    --warning-red: #d40000;
    --panel: #f3f1fa;
  }
  html, body {
    margin: 0;
    padding: 0;
    width: 993px;
    height: 1200px;
    overflow: hidden;
    background: #ffffff;
  }
  .canvas {
    position: relative;
    width: 993px;
    height: 1200px;
    font-family: "Tinos", "Times New Roman", serif;
    color: var(--ink);
  }
  .frame {
    position: absolute;
    inset: 0;
  }
  .bedroom-photo {
    position: absolute;
    left: 120px;
    top: 330px;
    width: 760px;
    height: 560px;
    background:
      radial-gradient(ellipse 60% 45% at 50% 40%, rgba(255,255,255,0.85), rgba(255,255,255,0) 70%),
      linear-gradient(180deg, rgba(226,214,236,0.55), rgba(238,230,244,0.7) 60%, rgba(230,222,244,0.3));
    border-radius: 30px;
  }
  .flower-field {
    position: absolute;
    left: 84px;
    top: 880px;
    width: 806px;
    height: 200px;
    background:
      radial-gradient(circle at 10% 70%, rgba(255,255,255,0.8), rgba(255,255,255,0) 18%),
      radial-gradient(circle at 55% 85%, rgba(250,210,240,0.7), rgba(250,210,240,0) 30%),
      linear-gradient(180deg, rgba(220,210,245,0), rgba(206,190,240,0.75));
  }
  .brand {
    position: absolute;
    left: 0;
    right: 0;
    top: 190px;
    text-align: center;
    font-size: 64px;
    font-weight: 400;
    color: var(--brand-ink);
    letter-spacing: 1px;
  }
  .rule {
    position: absolute;
    left: 95px;
    width: 773px;
    height: 3px;
    background: var(--rule);
  }
  .rule--upper { top: 325px; }
  .rule--lower { top: 339px; }
  .copy {
    position: absolute;
    left: 115px;
    top: 363px;
    width: 740px;
    font-size: 16.4px;
    line-height: 22.4px;
  }
  .copy p { margin: 0 0 22.4px; }
  .copy p.tight { margin-bottom: 0; }
  .copy .section-title {
    color: var(--heading-blue);
    margin-bottom: 22.4px;
  }
  .notice {
    position: absolute;
    left: 84px;
    width: 826px;
    text-align: center;
    font-weight: 700;
  }
  .notice--age { top: 942px; font-size: 18.5px; }
  .notice--warning { top: 965px; font-size: 18.5px; font-weight: 400; color: var(--warning-red); }
  .notice--choking { top: 989px; font-size: 18px; }
</style>
</head>
<body>
<div class="canvas">
  <svg class="frame" width="993" height="1200" viewBox="0 0 993 1200" aria-hidden="true">
    <defs>
      <linearGradient id="panelFill" x1="0" y1="0" x2="0" y2="1">
        <stop offset="0" stop-color="#f6f4fb"/>
        <stop offset="0.5" stop-color="#f1eff9"/>
        <stop offset="1" stop-color="#e6def5"/>
      </linearGradient>
      <linearGradient id="tealTab" x1="0" y1="0" x2="1" y2="1">
        <stop offset="0" stop-color="var(--teal-light)"/>
        <stop offset="1" stop-color="var(--teal)"/>
      </linearGradient>
      <linearGradient id="skyBand" x1="0" y1="0" x2="0" y2="1">
        <stop offset="0" stop-color="#7cc4e3"/>
        <stop offset="0.5" stop-color="#e8f6fc"/>
        <stop offset="1" stop-color="#7cc4e3"/>
      </linearGradient>
      <linearGradient id="limeBand" x1="0" y1="0" x2="0" y2="1">
        <stop offset="0" stop-color="#c4dc78"/>
        <stop offset="0.5" stop-color="#f4f9df"/>
        <stop offset="1" stop-color="#c4dc78"/>
      </linearGradient>
    </defs>
    <!-- card body -->
    <rect x="82" y="15" width="810" height="1172" rx="90" fill="url(#panelFill)" stroke="#d4d4d4" stroke-width="2"/>
    <!-- top bands -->
    <rect x="178" y="15" width="617" height="60" fill="#f6f2fa"/>
    <rect x="178" y="28" width="617" height="44" fill="url(#limeBand)"/>
    <rect x="178" y="85" width="617" height="40" fill="url(#skyBand)"/>
    <!-- bottom bands -->
    <rect x="178" y="1080" width="617" height="40" fill="url(#skyBand)"/>
    <rect x="178" y="1132" width="617" height="44" fill="url(#limeBand)"/>
    <!-- corner tabs -->
    <path d="M82 130 Q82 15 180 15 L180 85 Q110 95 95 140 Z" fill="url(#tealTab)"/>
    <path d="M892 130 Q892 15 795 15 L795 85 Q865 95 880 140 Z" fill="url(#tealTab)"/>
    <path d="M82 1070 Q82 1187 180 1187 L180 1120 Q110 1110 95 1060 Z" fill="url(#tealTab)"/>
    <path d="M892 1070 Q892 1187 795 1187 L795 1120 Q865 1110 880 1060 Z" fill="url(#tealTab)"/>
  </svg>

  <div class="bedroom-photo" role="img" aria-label="Soft faded photo of a couple sleeping peacefully on white pillows"></div>
  <div class="flower-field" role="img" aria-label="Soft pastel pink and lilac flower pattern along the bottom"></div>

  <div class="brand">BrindleGoods</div>
  <div class="rule rule--upper"></div>
  <div class="rule rule--lower"></div>

  <div class="copy">
    <p>During sleep our breathing meets resistance in the first 5-10 mm of the nasal cavity. A narrow nasal passage way is one the main causes for snoring which interferes with an optimal night’s rest. BrindleGoods anti snore aid makes breathing easier and in doing so will prevent snoring in many cases.</p>
    <p>The BrindleGoods anti snore aid is made from medical grade silicone in accordance with<br>European and American guidelines.</p>
    <p>The Brindle Goods anti snore aid is flexible, soft, and skin-friendly and will generally not cause irritation or damage to the mucous membrane or the skin of the nose. Normal soap is all that is needed for cleaning it.</p>
    <p class="section-title">Instructions for use:</p>
    <p class="tight"><span>BEFORE USE-</span> the BrindleGoods anti snore aid should be washed with soap and lukewarm water after being removed from its packaging.&nbsp; Be sure to rinse well and remove any soap remaining as it may be unpleasant for sensitive mucous membrane.</p>
    <p>FIND THE RIGHT FIT- There is 4 sizes. Select the size which fits your nostrils most comfortably.<br>If the width feels good but is too deep for your liking, a simple scissors can be used along the ringed edges to shorten it. Shorten the pipes a minimal amount initially, until you find the correct length.</p>
    <p class="tight">BrindleGoods anti snore aid ensures that the nostrils remain open, allowing sufficient air to flow freely in and out allowing you to sleep in any position you wish.<br>If the BrindleGoods anti snoring aid doesn't help reduce your snoring at all you may want to consider consulting a specialist doctor.<br>STOP USE- in case of skin/mucosal irritation. Do not exceed recommended duration of use. Seek medical attention for abnormal breathing patterns during sleep, daytime sleepiness,difficulty in breathing etc.</p>
  </div>

  <div class="notice notice--age">THIS PRODUCT IS NOT INTENDED FOR USE BY CHILDEREN 5 AND UNDER</div>
  <div class="notice notice--warning">WARNING</div>
  <div class="notice notice--choking">CHOKING HAZARD - Small Parts. Not for children under 3 years.</div>
</div>
</body>
</html>
```